Business Card Design - Corporate

Create a sleek elegant business card layout while suggesting a color scheme. Convey cutting edge technology while maintaining a corporate feel that is easily readable.

Company designs and manufactures consumer electronic products for mass retail that are mainly app driven.

(vector logo and die-line provided)

Target Market(s)

Corporate level, tech industry.

Industry/Entity Type

Business

Contact Information for Business Card

Generic Info:

Name
Title
email
address
phone 1
phone 2
website (quillbarn.com) on back

Font styles to use
Sans Serif

Requirements
Must have
• At least 2 colors + white on one side.
Nice to have
• Solid suggestion on color for logo and overall design. Color flood on back of card.
Should not have
• background texture like... marble, stone, patterns or circuit boards

```html
<!DOCTYPE html>
<html lang="en">
<head>
<meta charset="utf-8">
<title>Quillbarn Business Card</title>
<link rel="stylesheet" href="https://fonts.googleapis.com/css2?family=Open+Sans:wght@400;700&display=swap">
<style>
  :root {
    --page: #ecebea;
    --card-white: #f7f7f7;
    --card-grey-top: #8a8a8a;
    --card-grey-bottom: #5c5c5c;
    --brand-red: #e3131b;
    --wordmark-grey: #6d6d6d;
    --text-light: #f2f2f2;
    --icon-cut: #6a6a6a;
  }
  * { margin: 0; padding: 0; box-sizing: border-box; }
  html, body { width: 1200px; height: 902px; overflow: hidden; }
  body {
    background: var(--page);
    font-family: "Open Sans", Arial, sans-serif;
    display: flex;
    align-items: center;
    justify-content: center;
    gap: 48px;
  }
  .card {
    position: relative;
    width: 540px;
    height: 310px;
    border-radius: 26px;
    overflow: hidden;
    box-shadow: 0 10px 28px rgba(0,0,0,0.22);
  }
  .card-front { background: var(--card-white); }
  .card-back { background: linear-gradient(160deg, var(--card-grey-top), var(--card-grey-bottom)); }

  .wordmark {
    position: absolute;
    left: 0; right: 0; top: 122px;
    text-align: center;
    font-size: 58px;
    font-weight: 400;
    letter-spacing: 8px;
    color: var(--wordmark-grey);
  }

  .person {
    position: absolute;
    left: 40px; top: 120px;
  }
  .person-name {
    font-size: 30px;
    font-weight: 700;
    color: var(--brand-red);
    line-height: 1.1;
  }
  .person-title {
    font-size: 15px;
    color: var(--text-light);
    margin-left: 96px;
  }
  .contact-list {
    position: absolute;
    left: 40px; bottom: 26px;
    list-style: none;
  }
  .contact-item {
    display: flex;
    align-items: center;
    gap: 10px;
    font-size: 14px;
    color: var(--text-light);
    line-height: 24px;
  }
  .contact-item svg { width: 15px; height: 15px; fill: var(--brand-red); flex: none; }
</style>
</head>
<body>
  <section class="card card-front">
    <div class="wordmark">QUILLBARN</div>
  </section>

  <section class="card card-back">
    <div class="person">
      <div class="person-name">Mark Ellison</div>
      <div class="person-title">Designation</div>
    </div>
    <ul class="contact-list">
      <li class="contact-item">
        <svg viewBox="0 0 16 16"><rect x="1" y="3" width="14" height="10" rx="1"/><path d="M1 4l7 5 7-5" stroke="#6a6a6a" stroke-width="1.4" fill="none"/></svg>
        info@quillbarn.com
      </li>
      <li class="contact-item">
        <svg viewBox="0 0 16 16"><path d="M8 1l7 6h-2v8H3V7H1z"/></svg>
        Your address goes here, 11000
      </li>
      <li class="contact-item">
        <svg viewBox="0 0 16 16"><path d="M4 1l3 3-2 2c1 2 3 4 5 5l2-2 3 3-2 3C7 15 1 9 1 3z"/></svg>
        000 000 0000 / 000 000 0001
      </li>
      <li class="contact-item">
        <svg viewBox="0 0 16 16"><circle cx="8" cy="8" r="7"/><path d="M1 8h14M8 1c-3 4-3 10 0 14M8 1c3 4 3 10 0 14" stroke="#6a6a6a" stroke-width="1.2" fill="none"/></svg>
        www.quillbarn.com
      </li>
    </ul>
  </section>
</body>
</html>
```